Flyer für ein soziales Dienstleistungsunternehmen
Zielgruppe
Wir sind ein soziales Dienstleistungsunternehmen, welches versucht durch Workshops und Vorträge für Kinder, Jugendliche und deren Betreuungspersonen (auch Lehrkräfte, Erzieher/innen, Eltern, usw.) Prävention und Aufklärung bezüglich mentale Gesundheit zu betreiben und so auch Entstigmatisierung zu ermöglichen. Wir möchten einen allgemeinen Flyer erstellen, der für Schulen, Kindergärten und andere Einrichtungen, aber auch Eltern und Ämter interessant ist.
Aufgabenstellung
-vorhandenes Logo soll integriert werden, Farbe und Gestaltung daran anpassen
-Platz lassen für Slogan
-überschaubar, Überblick über unsere Angebote (Texte liefern wir selbst)
-ansprechend und Interesse weckend
-nicht 0815/Standard mentale Gesundheit-Flyer bitte :)
-modern, locker, dynamisch, jugendlich

```html
<!DOCTYPE html>
<html lang="de">
<head>
<meta charset="utf-8">
<title>Sozialwerk – Flyer</title>
<link rel="stylesheet" href="https://fonts.googleapis.com/css2?family=Oswald:wght@500;600&family=Raleway:wght@400;500;600&display=swap">
<style>
  :root {
    --orange: #ec7731;
    --teal: #3c7a85;
    --mint: #8fd1c2;
    --ink: #1f2a2e;
    --paper: #ffffff;
    --stage: #d4d4d4;
    --head: "Oswald", "Arial Narrow", sans-serif;
    --body: "Raleway", Arial, sans-serif;
  }
  * { box-sizing: border-box; margin: 0; padding: 0; }
  html, body { width: 1200px; height: 848px; overflow: hidden; }
  body {
    background: var(--stage);
    font-family: var(--body);
    position: relative;
  }
  .spread {
    position: absolute;
    top: 219px;
    width: 580px;
    height: 410px;
    display: flex;
    background: var(--paper);
    box-shadow: 0 6px 18px rgba(0,0,0,.18);
  }
  .spread--inside { left: 13px; }
  .spread--outside { left: 607px; }
  .panel {
    position: relative;
    width: 193.33px;
    height: 100%;
    overflow: hidden;
  }
  .panel--orange { background: var(--orange); }
  .panel--white { background: var(--paper); }
  .panel--mint { background: var(--mint); }
  .panel--teal-lower { background: var(--paper); }

  .photo { position: absolute; }
  .photo--circle { border-radius: 50%; }

  .heading {
    position: absolute;
    font-family: var(--head);
    font-weight: 600;
    font-size: 15px;
    letter-spacing: 2.4px;
    line-height: 1;
    white-space: nowrap;
  }
  .heading--vertical {
    transform: rotate(-90deg);
    transform-origin: left top;
  }
  .bar { position: absolute; }

  .copy {
    position: absolute;
    font-size: 6.4px;
    line-height: 9.2px;
  }
  .copy--light { color: #fff; }
  .copy--dark { color: var(--ink); }
  .bullets {
    list-style: none;
    margin-top: 8px;
    padding-left: 14px;
  }
  .bullets li { position: relative; }
  .bullets li::before {
    content: "·";
    position: absolute;
    left: -13px;
  }

  .teal-block {
    position: absolute;
    inset: 0;
    background: var(--teal);
    clip-path: polygon(0 160px, 100% 196px, 100% 100%, 0 100%);
  }

  .contact {
    position: absolute;
    left: 70px;
    top: 208px;
    font-size: 6.6px;
    line-height: 9.4px;
    color: var(--ink);
  }
  .contact b { font-weight: 600; }
  .website {
    position: absolute;
    left: 70px;
    top: 256px;
    font-family: var(--head);
    font-weight: 500;
    font-size: 5.6px;
    color: var(--ink);
  }

  .brand {
    position: absolute;
    left: 0;
    width: 100%;
    top: 44px;
    text-align: center;
    font-family: var(--body);
    font-weight: 600;
    font-size: 13px;
    line-height: 16px;
    color: var(--teal);
  }
  .title {
    position: absolute;
    left: 0;
    width: 100%;
    top: 112px;
    text-align: center;
    padding-left: 3px;
    font-family: var(--head);
    font-weight: 600;
    font-size: 27px;
    letter-spacing: 3px;
    line-height: 1;
    white-space: nowrap;
    color: var(--mint);
    z-index: 2;
  }
</style>
</head>
<body>

<section class="spread spread--inside">

  <div class="panel panel--orange">
    <div class="photo photo--circle" role="img" aria-label="Foto: Eltern halten lächelndes Kleinkind"
         style="left:26px; top:4px; width:140px; height:140px; background:radial-gradient(circle at 45% 45%, #e9c6a8, #a88466 60%, #6e5a4c);"></div>
    <div class="copy copy--light" style="left:22px; top:163px; width:152px;">
      <p>Fic temperf eritatus est, asperio ma aceriant aliquam etur apidundiatus am, omnis pedit apero eos enditatur, adis adida hekno acculluOptat. Agnimol oriorum intem voluptas eniendu sandebit ipsum commo ex et mos aborum quis magnimus dolupta.</p>
      <ul class="bullets">
        <li>Agnimol oriorum intem voluptas.</li>
        <li>Dolupta cuptionsequi options.</li>
        <li>Ullectintore magni con et.</li>
        <li>Optat agnimol oriorum intem volupts.</li>
      </ul>
    </div>
    <div class="bar" style="left:126px; top:307px; width:20px; height:3.5px; background:#fff;"></div>
    <div class="heading heading--vertical" style="left:152px; top:380px; color:#fff; font-size:14px;">ELTERN</div>
  </div>

  <div class="panel panel--white">
    <div class="heading" style="left:24px; top:112px; color:var(--teal);">SCHÜLER</div>
    <div class="bar" style="left:24px; top:143px; width:20px; height:3.5px; background:var(--teal);"></div>
    <div class="copy copy--dark" style="left:56px; top:137px; width:126px;">
      <p>Fic temperf eritatus est, asperio ma aceriant aliquam etur apidundiatus am, omnis pedit apero eos enditatur, adis accullu.Ur, te vera nes nim ipsam dolupie nienduntia que molor rerspie nimolorpos as ad ut doluptate rem re net elibus, susa volorpores magnisit, con corum re nectatemo ex earum et volore que con ped quiasperum faceaquam dolupti ommodit, quiscia volorro blaborit, il ipienis trumene cesequam ea nobis sundunt re consequi anda simus ipiende geurh alkeeh posa.</p>
    </div>
    <div class="photo" role="img" aria-label="Foto: Schüler mit Rucksack im Klassenzimmer"
         style="inset:0; clip-path:polygon(0 306px, 100% 246px, 100% 100%, 0 100%); background:linear-gradient(160deg, #f1ede6 0%, #d9cdb9 55%, #b89a78 100%);"></div>
  </div>

  <div class="panel panel--teal-lower">
    <div class="photo" role="img" aria-label="Foto: Mädchen mit Brille sitzt am Fenster"
         style="inset:0; clip-path:polygon(0 0, 100% 0, 100% 196px, 0 160px); background:linear-gradient(135deg, #f3f4f2 0%, #d9dcd6 45%, #9fb9cf 75%, #8e7a66 100%);"></div>
    <div class="teal-block"></div>
    <div class="heading" style="left:64px; top:187px; color:var(--mint);">KINDER</div>
    <div class="bar" style="left:20px; top:226px; width:3.5px; height:20px; background:var(--mint);"></div>
    <div class="copy copy--light" style="left:32px; top:222px; width:152px;">
      <p>Fic temperf eritatus est, asperio ma aceriant aliquam etur apidundiatus am, omnis pedit apero eos enditatur, adis adida hekno acculluOptat. Agnimol oriorum intem voluptas eniendu sandebit ipsum commo ex et mos aborum quis magnimus dolupta.</p>
      <ul class="bullets">
        <li>Agnimol oriorum intem voluptas.</li>
        <li>Dolupta cuptionsequi options.</li>
        <li>Ullectintore magni con et.</li>
        <li>Optat agnimol oriorum intem volupts.</li>
      </ul>
    </div>
  </div>

</section>

<section class="spread spread--outside">

  <div class="panel panel--white">
    <div class="photo" role="img" aria-label="Foto: Lehrer vor der Tafel im Klassenraum"
         style="inset:0; clip-path:polygon(0 0, 100% 0, 100% 160px, 0 188px); background:linear-gradient(150deg, #2e2f2f 0%, #4a4a46 45%, #b79a78 80%, #d7b58c 100%);"></div>
    <div class="heading heading--vertical" style="left:24px; top:256px; color:var(--orange); font-size:14px;">LEHRER</div>
    <div class="bar" style="left:24px; top:262px; width:13px; height:4px; background:var(--orange);"></div>
    <div class="copy copy--dark" style="left:48px; top:208px; width:128px;">
      <p>Fic temperf eritatus est, asperio ma aceriant aliquam etur apidundiatus am, omnis pedit apero eos enditatur, adis accullu.Ur, te vera nes nim ipsam dolupie nienduntia que molor rerspie nimolorpos as ad ut doluptate rem re net elibus, susa volorpores magnisit, con corum re nectatemo ex earum et volore que con ped quiasperum faceaquam dolupti ommodit, quiscia volorro blaborit, il ipienis trumene cesequam ea nobis sundunt re consequi anda simus ipiende geurh alkeeh posa.</p>
    </div>
  </div>

  <div class="panel panel--mint">
    <div class="bar" style="left:0; top:119px; width:20px; height:3.5px; background:var(--teal);"></div>
    <div class="heading" style="left:28px; top:112px; color:var(--teal);">KONTAKT</div>
    <div class="copy copy--dark" style="left:22px; top:150px; width:152px;">
      <p>Fic temperf eritatus est, asperio ma aceriant aliquam etur apidundiatus am, omnis pedit apero eos enditatur, adis adida hekno accullu.</p>
    </div>
    <div class="contact">
      <p><b>P:</b> +01 234 567 890</p>
      <p><b>E:</b> yourinfo@website.com</p>
      <p><b>A:</b> Strasse 123</p>
      <p>12345 Stadt</p>
    </div>
    <div class="website">www.yourwebsite.com</div>
    <div class="photo photo--circle" role="img" aria-label="Foto: Beraterin im Gespräch mit einer Person"
         style="left:30px; top:305px; width:138px; height:138px; background:radial-gradient(circle at 50% 40%, #efe6de, #cdbfb2 55%, #8f8a86);"></div>
  </div>

  <div class="panel panel--white">
    <div class="brand">Lindner<br>&amp; Haupt</div>
    <h1 class="title">SOZIALWERK</h1>
    <div class="photo" role="img" aria-label="Foto: Jugendliche im grünen Hoodie sitzt im Klassenzimmer"
         style="left:40px; top:134px; width:110px; height:200px; background:linear-gradient(170deg, #e9e6e0 0%, #b9c8b8 40%, #9fc4a8 55%, #b29c7e 85%, #8c7358 100%);"></div>
  </div>

</section>

</body>
</html>
```